7 Vex Label

Design a label for 7 Vex styling gels. The logo is attached. The color is C=100, M=100, Y=0, K=0. The 16 oz. jar is also attached.

Updates

Attention all designers,

The old logo has been deleted.  I have uploaded a new logo for this project.  Can you please update your design with the NEW LOGO?
thank you,
Rob

Target Market(s)

Multicultural

Requirements
Must have
• you must used the logo attached.

text to be included on the jar:

Used by Professionals
Maximum Hold
Alcohol Free
NO FLAKING

16 oz.

As far as label size, use the jar photo, and fit the design on it.

```html
<!DOCTYPE html>
<html lang="en">
<head>
<meta charset="UTF-8">
<title>7 Vex Styling Gel Label</title>
<link href="https://fonts.googleapis.com/css2?family=Arimo:wght@400;700&family=Permanent+Marker&family=Tinos:wght@700&display=swap" rel="stylesheet">
<style>
  :root {
    --page: #ececec;
    --label-deep: #0b0a24;
    --label-indigo: #1c1553;
    --label-violet: #4a1f86;
    --ink: #ffffff;
  }
  * { margin: 0; padding: 0; box-sizing: border-box; }
  html, body {
    width: 1020px;
    height: 1200px;
    overflow: hidden;
    background: var(--page);
  }
  .label {
    position: absolute;
    left: 80px;
    top: 55px;
    width: 860px;
    height: 1090px;
    overflow: hidden;
    background: var(--label-deep);
    color: var(--ink);
  }
  .label__light {
    position: absolute;
    inset: 0;
    background:
      radial-gradient(ellipse 30% 60% at 62% 18%, rgba(240,138,44,0.55), transparent 70%),
      radial-gradient(ellipse 35% 70% at 48% 55%, rgba(192,48,143,0.5), transparent 72%),
      radial-gradient(ellipse 40% 60% at 45% 95%, rgba(45,72,200,0.55), transparent 70%),
      linear-gradient(90deg, var(--label-deep) 0%, var(--label-indigo) 45%, var(--label-violet) 100%);
  }
  .brand {
    position: absolute;
    left: 0;
    right: 0;
    top: 250px;
    text-align: center;
    font-family: "Arimo", Arial, sans-serif;
    font-weight: 700;
    font-size: 150px;
    line-height: 1;
    letter-spacing: 4px;
    white-space: nowrap;
  }
  .tagline {
    position: absolute;
    left: 0;
    right: 0;
    top: 600px;
    text-align: center;
    font-family: "Permanent Marker", cursive;
    font-size: 46px;
    letter-spacing: 3px;
    white-space: nowrap;
    transform: rotate(-2deg);
  }
  .claims {
    position: absolute;
    left: 0;
    right: 0;
    top: 720px;
    text-align: center;
    list-style: none;
    font-family: "Arimo", Arial, sans-serif;
    font-size: 54px;
    line-height: 66px;
  }
  .size {
    position: absolute;
    left: 0;
    right: 0;
    top: 965px;
    text-align: center;
    font-family: "Tinos", "Times New Roman", serif;
    font-weight: 700;
    font-size: 60px;
    letter-spacing: 2px;
  }
</style>
</head>
<body>
  <main class="label">
    <div class="label__light" role="img" aria-label="Swirling streaks of orange, magenta and blue light across a dark indigo background"></div>

    <p class="brand">7 Vex</p>

    <p class="tagline">USED BY PROFESSIONALS</p>

    <ul class="claims">
      <li>Maximum Hold</li>
      <li>Alcohol Free</li>
      <li>NO FLAKING</li>
    </ul>

    <p class="size">16 oz.</p>
  </main>
</body>
</html>
```